Night Dresses business cards business requirers

We are a new company initiating Mexico operations. Our core business is Night woman dress (both formal and party dress) for rent. Gownhaven is the name of the company. ITS Gownhaven form by two word. The dress word and topia (Utopic) so the place Gownhaven Means That You cant get the ideal, perfect and unique dress for your event. So we would like a modern, very creative, and attractive business card.

Industry/Entity Type

Womens Clothing

Contact Information for Business Card

Rounded Borders, two faces

Requirements
Must have
• Rounded borders, logo and slogan, modern, glam, attractive design
Should not have
• modern design classic or not

```html
<!DOCTYPE html>
<html lang="en">
<head>
<meta charset="utf-8">
<title>Gownhaven Business Card</title>
<link rel="stylesheet" href="https://fonts.googleapis.com/css2?family=Josefin+Sans:wght@400;600&family=Roboto:wght@400;700&display=swap">
<style>
  :root {
    --backdrop: #e4e4e4;
    --charcoal: #525156;
    --charcoal-dark: #3f3e43;
    --orchid: #a8518a;
    --ink: #3a3a3a;
    --paper: #ffffff;
  }
  * { margin: 0; padding: 0; box-sizing: border-box; }
  html, body {
    width: 1200px; height: 576px; overflow: hidden;
    background: var(--backdrop);
  }
  .canvas { position: relative; width: 1200px; height: 576px; }
  .card {
    position: absolute; top: 138px;
    width: 484px; height: 292px;
    border-radius: 13px; overflow: hidden;
  }
  .card-back {
    left: 82px;
    background: linear-gradient(180deg, var(--charcoal) 0%, var(--charcoal-dark) 100%);
  }
  .wordmark {
    font-family: "Josefin Sans", sans-serif; font-weight: 400;
    text-transform: uppercase; white-space: nowrap;
  }
  .tagline {
    font-family: "Josefin Sans", sans-serif; font-weight: 400;
    white-space: nowrap;
  }
  .card-back .wordmark {
    position: absolute; left: 0; width: 100%; top: 124px;
    text-align: center; color: var(--paper);
    font-size: 31px; letter-spacing: 6px;
  }
  .card-back .tagline {
    position: absolute; left: 0; width: 100%; top: 164px;
    text-align: center; color: var(--paper);
    font-size: 14px; letter-spacing: 1px;
  }

  .card-front { left: 602px; background: var(--paper); }
  .holder { position: absolute; left: 23px; top: 44px; font-family: "Roboto", sans-serif; }
  .holder-name { color: var(--orchid); font-weight: 700; font-size: 20px; }
  .holder-role { color: var(--ink); font-size: 11.5px; margin-top: 3px; }
  .brand-block {
    position: absolute; right: 24px; top: 116px;
    display: flex; flex-direction: column; align-items: center;
  }
  .card-front .wordmark { color: var(--ink); font-size: 17px; letter-spacing: 4px; }
  .card-front .tagline {
    color: var(--ink); font-size: 10px; letter-spacing: 0.6px; margin-top: 5px;
  }
  .contact-list {
    position: absolute; left: 27px; top: 172px; list-style: none;
    font-family: "Roboto", sans-serif; font-size: 12px; color: var(--ink);
  }
  .contact-list li { display: flex; align-items: center; height: 17px; }
  .contact-list svg { width: 11px; height: 11px; margin-right: 12px; fill: var(--orchid); }
  .wave { position: absolute; left: 0; top: 0; width: 484px; height: 292px; }
  .address {
    position: absolute; right: 26px; top: 235px; text-align: right;
    font-family: "Roboto", sans-serif; font-size: 12px; line-height: 17px;
    font-style: normal; color: var(--paper);
  }
</style>
</head>
<body>
<main class="canvas">
  <section class="card card-back" aria-label="Card back">
    <div class="wordmark">Gownhaven</div>
    <div class="tagline">Gowns on loan</div>
  </section>

  <section class="card card-front" aria-label="Card front">
    <svg class="wave" viewBox="0 0 484 292" aria-hidden="true">
      <path d="M0,292 L0,272 C120,284 220,270 300,240 C370,212 430,193 484,189 L484,292 Z" fill="var(--orchid)"/>
      <path d="M0,244 C60,260 150,276 230,266 C320,254 400,200 484,168 L484,178 C410,206 330,262 240,276 C150,290 60,278 0,262 Z" fill="var(--charcoal)"/>
      <path d="M60,252 C140,268 220,270 300,246" stroke="var(--paper)" stroke-width="1.2" fill="none" opacity="0.7"/>
    </svg>

    <div class="holder">
      <div class="holder-name">Elena Marquez</div>
      <div class="holder-role">Managing Director</div>
    </div>

    <div class="brand-block">
      <div class="wordmark">Gownhaven</div>
      <div class="tagline">Gowns on loan</div>
    </div>

    <ul class="contact-list">
      <li><svg viewBox="0 0 12 12"><path d="M1 3 Q6 0 11 3 L10 5 L8 4.5 L8 3.8 Q6 3.2 4 3.8 L4 4.5 L2 5 Z M3 6 H9 L10 11 H2 Z"/></svg>1300 418 752</li>
      <li><svg viewBox="0 0 12 12"><path d="M6 0.5 A5.5 5.5 0 1 0 6 11.5 A5.5 5.5 0 1 0 6 0.5 Z M6 1.8 C7.2 3 7.6 4.5 7.7 5.4 H4.3 C4.4 4.5 4.8 3 6 1.8 Z M1.9 6.6 H3.3 C3.4 7.8 3.8 9 4.5 10 A4.3 4.3 0 0 1 1.9 6.6 Z M4.3 6.6 H7.7 C7.6 7.6 7.2 9 6 10.2 C4.8 9 4.4 7.6 4.3 6.6 Z M8.7 6.6 H10.1 A4.3 4.3 0 0 1 7.5 10 C8.2 9 8.6 7.8 8.7 6.6 Z M1.9 5.4 A4.3 4.3 0 0 1 4.5 2 C3.8 3 3.4 4.2 3.3 5.4 Z M8.7 5.4 C8.6 4.2 8.2 3 7.5 2 A4.3 4.3 0 0 1 10.1 5.4 Z"/></svg>www.gownhaven-rentals.com</li>
      <li><svg viewBox="0 0 12 12"><path d="M0.5 2.5 H11.5 V9.5 H0.5 Z M1.5 3.5 L6 7 L10.5 3.5" stroke="var(--paper)" stroke-width="0.9"/></svg>elena.marquez@gownhaven-rentals.com</li>
    </ul>

    <address class="address">48 Jacaranda Lane,<br>Mexico City CDMX 06700</address>
  </section>
</main>
</body>
</html>
```